Coffee bag stamp design for new coffee brand

Stamp design that will be used like a label on a coffee package.
It must be a vector that can be produced as a stamp. Coffee bag is from brown craft paper. I upload image of this bag. Size of design is 80mm x 140mm.
I also uploaded two pictures for inspiration, but I will also appreciate new ideas.

Target Market(s)

Coffee lovers, who love to try new coffee. Also hipsters.

Colors

Designer to choose only greyscale colors for use in the design.

Requirements
Must have
• Some information about coffee must have:
Name: BRAZIL (the biggest font in that design)
Region: Santos
Altitude: 60 – 1200 m.n.m.
Variety: Arabica
Processing: unwashed

```html
<!DOCTYPE html>
<html lang="en">
<head>
<meta charset="UTF-8">
<title>Lotara Coffee – Brazil Label</title>
<link rel="stylesheet" href="https://fonts.googleapis.com/css2?family=League+Spartan:wght@700&family=Oswald:wght@300;400&display=swap">
<style>
  :root {
    --ink: #111111;
    --paper: #ffffff;
  }
  * { margin: 0; padding: 0; box-sizing: border-box; }
  html, body { width: 686px; height: 1200px; overflow: hidden; background: var(--paper); }
  .label { position: relative; width: 686px; height: 1200px; color: var(--ink); font-family: "Oswald", sans-serif; font-weight: 300; }
  .frame { position: absolute; inset: 0; }
  .brand {
    position: absolute; left: 0; width: 686px; text-align: center;
    font-family: "League Spartan", sans-serif; font-weight: 700; color: var(--ink);
  }
  .brand-name { top: 322px; font-size: 84px; letter-spacing: 3px; line-height: 1; }
  .brand-sub { top: 406px; font-size: 46px; letter-spacing: 2px; line-height: 1; }
  .origin {
    position: absolute; top: 600px; left: 0; width: 686px; text-align: center;
    font-family: "League Spartan", sans-serif; font-weight: 700;
    font-size: 96px; letter-spacing: 9px; line-height: 1; padding-left: 9px;
  }
  .side-note {
    position: absolute; font-size: 9px; letter-spacing: 2.5px; white-space: nowrap; text-transform: uppercase; font-weight: 400;
  }
  .side-note.roast { left: 80px; top: 678px; transform-origin: 0 0; transform: rotate(-90deg); }
  .side-note.roast .hand { font-style: italic; font-size: 11px; margin-left: 12px; letter-spacing: 1px; font-weight: 300; }
  .side-note.type { left: 600px; top: 574px; transform-origin: 0 0; transform: rotate(90deg); }
  .spec { position: absolute; text-transform: uppercase; }
  .spec .key { display: block; font-size: 8.5px; letter-spacing: 1.8px; font-weight: 400; }
  .spec .val { display: block; font-size: 17px; letter-spacing: 3px; margin-top: 6px; }
  .flavor-title { position: absolute; top: 1090px; right: 105px; font-size: 8.5px; letter-spacing: 1.8px; font-weight: 400; text-transform: uppercase; }
  .flavor-line { position: absolute; left: 96px; font-size: 15px; letter-spacing: 2.4px; text-transform: uppercase; white-space: nowrap; font-weight: 300; }
</style>
</head>
<body>
<div class="label">
  <svg class="frame" width="686" height="1200" viewBox="0 0 686 1200" fill="none" stroke="#111" stroke-width="2.5">
    <path d="M82,331 A260,254 0 0 1 602,331 L602,500 Q602,508 594,508 L580,508 Q574,508 574,514 L574,728 Q574,734 580,734 L594,734 Q602,734 602,742 L602,1036 Q602,1042 596,1042 L391.6,1042 A56,56 0 0 0 292.4,1042 L88,1042 Q82,1042 82,1036 L82,742 Q82,734 90,734 L103,734 Q109,734 109,728 L109,514 Q109,508 103,508 L90,508 Q82,508 82,500 Z"/>
    <path d="M286.4,1075 L88,1075 Q82,1075 82,1081 L82,1175 Q82,1181 88,1181 L596,1181 Q602,1181 602,1175 L602,1081 Q602,1075 596,1075 L397.6,1075 A56,56 0 0 1 286.4,1075"/>
    <circle cx="342" cy="320" r="198" stroke-width="16"/>
    <g stroke-width="2.2">
      <line x1="119" y1="825" x2="570" y2="825"/>
      <line x1="119" y1="890" x2="570" y2="890"/>
      <line x1="119" y1="957" x2="570" y2="957"/>
      <line x1="299" y1="825" x2="299" y2="890"/>
      <line x1="269" y1="890" x2="269" y2="957"/>
      <line x1="421" y1="890" x2="421" y2="957"/>
    </g>
  </svg>

  <div class="brand brand-name">LOTARA</div>
  <div class="brand brand-sub">COFFEE</div>

  <div class="side-note roast">Roast date:<span class="hand">7/12</span></div>
  <div class="side-note type">Type: whole bean</div>

  <h1 class="origin">BRAZIL</h1>

  <div class="spec" style="left:129px; top:834px;"><span class="key">Region</span><span class="val" style="margin-left:38px;">Santos</span></div>
  <div class="spec" style="left:313px; top:834px;"><span class="key">Altitude</span><span class="val" style="margin-left:53px;">60 – 1200 m.n.m.</span></div>
  <div class="spec" style="left:129px; top:899px;"><span class="key">Net wt.</span><span class="val" style="margin-left:23px;">12oz/340g</span></div>
  <div class="spec" style="left:282px; top:899px;"><span class="key">Variety</span><span class="val" style="margin-left:34px;">Arabica</span></div>
  <div class="spec" style="left:431px; top:899px;"><span class="key">Processing</span><span class="val" style="margin-left:23px;">Unwashed</span></div>

  <div class="flavor-title">Flavor profile</div>
  <p class="flavor-line" style="top:1108px;">Medium body and unique</p>
  <p class="flavor-line" style="top:1108px; left:390px;">aromatic qualities of</p>
  <p class="flavor-line" style="top:1128px;">spice and sweet.&nbsp; Distinctively mild, sweet, and mellow</p>
  <p class="flavor-line" style="top:1148px;">with gentle acidity.</p>
</div>
</body>
</html>
```